Need a sleek, professional business card design for a Web Development business

I need a unique business card designed for a web development company. It is also the parent company for any ventures I do, such as my ClipWave channel, startup ideas I have, etc. I am the single member of "Bright Harbor Code LLC." I will attach my basic logo here, so you will see the current color scheme and have the asset available. Thank you!

Target Market(s)

Startups, SMB's, Professionals

Industry/Entity Type

Business

Font styles to use
Other font styles liked:
• Lovello for headings is what I use, but not necessary.

Colors

Designer to choose colors to be used in the design.

Requirements
Nice to have
• Sleek is the word. Professional, modern, dark.
Should not have
• Any work from someone else's design. Lacking originality.

```html
<!DOCTYPE html>
<html lang="en">
<head>
<meta charset="utf-8">
<title>Bright Harbor Code LLC – Business Card</title>
<link href="https://fonts.googleapis.com/css2?family=Josefin+Sans:wght@700&family=Montserrat:wght@500;600&display=swap" rel="stylesheet">
<style>
  :root {
    --stage: #0f0f0f;
    --card: #262626;
    --pink: #ee5f70;
    --orange: #fba65f;
    --heading-font: "Josefin Sans", sans-serif;
    --body-font: "Montserrat", sans-serif;
  }
  html, body {
    margin: 0;
    width: 1200px;
    height: 1000px;
    overflow: hidden;
    background: var(--stage);
  }
  .stage {
    position: relative;
    width: 1200px;
    height: 1000px;
  }
  .card {
    position: absolute;
    width: 525px;
    height: 300px;
    border-radius: 18px;
    background: var(--card);
    overflow: hidden;
    box-shadow: 0 18px 40px rgba(0,0,0,.55);
  }
  .card--front { left: 50px; top: 200px; }
  .card--back  { left: 625px; top: 500px; }
  .card__accents {
    position: absolute;
    inset: 0;
    width: 100%;
    height: 100%;
  }

  /* Brand name placeholder where the mark sits */
  .brand-mark {
    position: absolute;
    display: flex;
    align-items: center;
    gap: 12px;
  }
  .brand-mark__square {
    width: 34px;
    height: 34px;
    border-radius: 6px;
    background: var(--orange);
    flex: none;
  }
  .brand-mark__name {
    font-family: var(--heading-font);
    font-weight: 700;
    font-size: 20px;
    line-height: 1.1;
    letter-spacing: .04em;
    text-transform: uppercase;
    color: var(--orange);
  }
  .card--front .brand-mark { left: 38px; top: 118px; width: 200px; }
  .card--back .brand-mark { right: 40px; bottom: 58px; width: 190px; }

  /* Front contact block */
  .contact {
    position: absolute;
    left: 268px;
    top: 96px;
    font-family: var(--body-font);
    color: var(--orange);
  }
  .contact__name {
    margin: 0;
    font-family: var(--heading-font);
    font-weight: 700;
    font-size: 21px;
    letter-spacing: .05em;
    color: var(--pink);
  }
  .contact__title {
    margin: 2px 0 16px;
    font-size: 14px;
    font-weight: 500;
  }
  .contact__lines {
    margin: 0 0 12px;
    padding: 0;
    list-style: none;
    font-size: 12.5px;
    font-weight: 500;
    line-height: 1.35;
  }

  /* Back company name */
  .company-name {
    position: absolute;
    left: 44px;
    top: 122px;
    margin: 0;
    font-family: var(--heading-font);
    font-weight: 700;
    font-size: 24px;
    letter-spacing: .05em;
    text-transform: uppercase;
    color: var(--pink);
  }
</style>
</head>
<body>
<main class="stage">

  <section class="card card--front" aria-label="Business card front">
    <svg class="card__accents" viewBox="0 0 525 300" aria-hidden="true">
      <defs>
        <linearGradient id="front-accent" x1="0" y1="0" x2="1" y2="0">
          <stop offset="0" stop-color="#ee5f70"/>
          <stop offset="1" stop-color="#fba65f"/>
        </linearGradient>
      </defs>
      <polyline points="290,0 316,30 525,30" fill="none" stroke="url(#front-accent)" stroke-width="5"/>
      <polygon points="0,250 200,250 230,300 0,300" fill="url(#front-accent)"/>
    </svg>

    <div class="brand-mark">
      <span class="brand-mark__square"></span>
      <span class="brand-mark__name">Bright Harbor Code</span>
    </div>

    <div class="contact">
      <h1 class="contact__name">LOREM IPSUM</h1>
      <p class="contact__title">President</p>
      <ul class="contact__lines">
        <li>Office 012 345 678</li>
        <li>Direct 987 654 321</li>
      </ul>
      <ul class="contact__lines">
        <li>youremail@domain.com</li>
        <li>www.yoursite.com</li>
      </ul>
    </div>
  </section>

  <section class="card card--back" aria-label="Business card back">
    <svg class="card__accents" viewBox="0 0 525 300" aria-hidden="true">
      <defs>
        <linearGradient id="back-accent" x1="0" y1="0" x2="1" y2="0">
          <stop offset="0" stop-color="#fba65f"/>
          <stop offset="1" stop-color="#ee5f70"/>
        </linearGradient>
      </defs>
      <polygon points="0,0 300,0 270,44 0,44" fill="url(#back-accent)"/>
      <polyline points="0,236 228,236 254,300" fill="none" stroke="url(#back-accent)" stroke-width="5"/>
    </svg>

    <h2 class="company-name">Bright Harbor Code LLC</h2>

    <div class="brand-mark">
      <span class="brand-mark__square"></span>
      <span class="brand-mark__name">Bright Harbor Code</span>
    </div>
  </section>

</main>
</body>
</html>
```